Oil and Gas Company: Letterhead Design

In short we need a professional company letterhead designed for our Oil and Gas company.

We would like to keep the design simple and professional. Letterhead to include the company logo and color scheme, front page and continuation pages.

For reference, see attached logo below with our company logo and color scheme.

Target Market(s)

Oil & Gas Market

Industry/Entity Type

Oil And Gas

Font styles to use
Sans Serif

Requirements
Must have
• Letterhead must contain a front page & continuation page.
• Must be simple and professional in design.
• Follow our logo and color scheme.
Nice to have
• I would like to have the logo embedded in the bottom right hand portion of the page to provide some depth into the letterhead.

```html
<!DOCTYPE html>
<html lang="en">
<head>
<meta charset="utf-8">
<title>Kestrel Ridge Energy Services – Letterhead</title>
<link rel="stylesheet" href="https://fonts.googleapis.com/css2?family=Jost:wght@500&family=Open+Sans:wght@400&display=swap">
<style>
  :root {
    --backdrop: #efefef;
    --paper: #e3e4e5;
    --brand-blue: #1552a0;
    --brand-red: #e0242c;
    --ink-dark: #1d2430;
    --ink-body: #6b6e72;
    --ink-sign: #3a3f48;
    --faint-mark: rgba(21, 82, 160, 0.08);
  }
  * { margin: 0; padding: 0; box-sizing: border-box; }
  html, body {
    width: 1006px;
    height: 1200px;
    overflow: hidden;
    background: var(--backdrop);
  }
  .letterhead {
    position: absolute;
    left: 189px;
    top: 185px;
    width: 622px;
    height: 822px;
    background: var(--paper);
    overflow: hidden;
  }
  .brand {
    position: absolute;
    top: 40px;
    left: 0;
    width: 100%;
    text-align: center;
  }
  .brand-square {
    display: block;
    width: 40px;
    height: 40px;
    margin: 0 auto 46px;
    background: var(--brand-blue);
  }
  .brand-name {
    font-family: "Jost", sans-serif;
    font-weight: 500;
    font-size: 16px;
    line-height: 18px;
    letter-spacing: 0.6px;
    color: var(--ink-dark);
    text-transform: uppercase;
  }
  .letter {
    position: absolute;
    top: 251px;
    left: 41px;
    width: 541px;
    font-family: "Open Sans", sans-serif;
    font-size: 11px;
    line-height: 17.2px;
    color: var(--ink-body);
  }
  .salutation { margin-bottom: 17px; }
  .letter-body p {
    text-align: justify;
    hyphens: auto;
    margin-bottom: 17px;
  }
  .closing { margin-top: 17px; }
  .signature {
    display: block;
    width: 92px;
    height: 28px;
    margin: 6px 0 6px;
    background: linear-gradient(90deg, rgba(58,63,72,0.35), rgba(58,63,72,0.15));
    border-radius: 14px;
  }
  .faint-mark {
    position: absolute;
    left: 432px;
    top: 606px;
    width: 170px;
    height: 170px;
    border-radius: 50%;
    background: var(--faint-mark);
  }
  .footer-band {
    position: absolute;
    left: 0;
    bottom: 0;
    width: 100%;
    height: 7px;
    display: flex;
    gap: 3px;
  }
  .footer-band .band-blue { flex: 0 0 437px; background: var(--brand-blue); }
  .footer-band .band-red { flex: 1; background: var(--brand-red); }
</style>
</head>
<body>
  <main class="letterhead">
    <header class="brand">
      <span class="brand-square"></span>
      <div class="brand-name">Kestrel Ridge<br>Energy Services</div>
    </header>

    <section class="letter">
      <div class="salutation">
        Dear Mr.Daniel ,<br>
        Subject :
      </div>
      <div class="letter-body">
        <p>Lorem Ipsum is simply dummy text of the printing and typesetting industry. Lorem Ipsum has been the industry's standard dummy text ever since the 1500s, when an unknown printer took a galley of type and scrambled it to make a type specimen book. It has survived not only five centuries, but also the leap into electronic typesetting, remaining essentially unchanged. It was popularised in the 1960s with the release of Letraset sheets containing Lorem Ipsum passages,</p>
        <p>and more recently with desktop publishing software like Aldus PageMaker including versions of Lorem Ipsum.Lorem Ipsum is simply dummy text of the printing and typesetting industry. Lorem Ipsum has been the industry's standard dummy text ever since the 1500s, when an unknown printer took a galley of type and scrambled it to make a type specimen book. It has survived not only five centuries, but also the leap into electronic typesetting, remaining essentially unchanged. It was popularised in the 1960s with the release of Letraset sheets containing Lorem Ipsum passages,</p>
        <p>and more recently with desktop publishing software like Aldus PageMaker including versions of Lorem Ipsum.he release of Letraset sheets containing Lorem Ipsum passages,he release of Letraset sheets containing Lorem Ipsum passages,</p>
      </div>
      <div class="closing">
        sincerely
        <span class="signature" role="img" aria-label="Handwritten signature of Daniel Hart"></span>
        Daniel Hart
      </div>
    </section>

    <div class="faint-mark" aria-hidden="true"></div>

    <footer class="footer-band" aria-hidden="true">
      <span class="band-blue"></span>
      <span class="band-red"></span>
    </footer>
  </main>
</body>
</html>
```